I need a new business card design for my pharmacy.

I need a business card design. I will include my logo.
The card needs to be readable. I prefer to have my logo on one side along with my website, the other side includes the other information. Please use combination of black, neon green, white, and silver. This needs to catch the eye but yet be clearly visible and legible. Thanks

Industry/Entity Type

Pharmacy

Contact Information for Business Card

It needs to have the following information listed:
Vel's Apothecary Owner/Pharm D.
7143 North Birch Lane
Sioux Falls, SD 57362
Phone 605-318-6027
Fax 605-318-6025
email: vel@velsapothecary.example
www.velsapothecary.example
Store hours Monday-Friday 8 am- 7 pm
Saturday 8 am- 12 pm
Sunday Closed
Please utilize the colors black, white, and neon green, maybe silver.

Requirements
Must have
• It needs to be easily readable!
Nice to have
• It should catch the eye.
Should not have
• Do not use any other colors except listed: black, neon green, white, & silver.

```html
<!DOCTYPE html>
<html lang="en">
<head>
<meta charset="utf-8">
<title>Vel's Apothecary – Business Card</title>
<link rel="stylesheet" href="https://fonts.googleapis.com/css2?family=Open+Sans:wght@400;600;700&display=swap">
<style>
  :root {
    --stage: #e9e9e7;
    --ink: #1f1f21;
    --ink-soft: #2b2b2e;
    --charcoal-light: #3a3c40;
    --white: #ffffff;
    --silver: #c9ccd0;
    --neon: #a8d32c;
    --photo-warm: #8a5a34;
    --photo-light: #d9d4c8;
    --photo-mid: #b9b2a6;
  }
  * { box-sizing: border-box; margin: 0; padding: 0; }
  html, body { width: 1200px; height: 780px; overflow: hidden; }
  body {
    background: var(--stage);
    font-family: "Open Sans", Arial, sans-serif;
    display: flex; align-items: center; justify-content: center; gap: 40px;
  }
  .card {
    position: relative; width: 540px; height: 309px; overflow: hidden;
    border-radius: 4px; box-shadow: 0 6px 18px rgba(0,0,0,.18);
  }
  /* Front */
  .card-front { background: linear-gradient(160deg, var(--ink-soft), var(--ink)); }
  .card-front .photo-band { position: absolute; inset: 0; width: 100%; height: 100%; }
  .contact { position: absolute; left: 268px; top: 34px; color: var(--white); }
  .contact .name { font-size: 28px; font-weight: 600; line-height: 1.1; }
  .contact .role { color: var(--neon); font-size: 15px; font-weight: 600; margin-bottom: 16px; }
  .contact .address { font-size: 14px; font-weight: 600; line-height: 1.35; margin-bottom: 4px; }
  .line { display: flex; align-items: center; gap: 7px; font-size: 14px; font-weight: 600; line-height: 1.5; }
  .icon { width: 14px; height: 14px; background: var(--neon); border-radius: 2px; display: inline-flex; align-items: center; justify-content: center; }
  .contact .web { color: var(--neon); font-size: 14px; font-weight: 600; margin-top: 16px; }
  /* Back */
  .card-back {
    background: radial-gradient(circle at 62% 45%, var(--charcoal-light), var(--ink) 78%);
    color: var(--white);
  }
  .brand { position: absolute; left: 40px; top: 62px; display: flex; align-items: center; gap: 22px; }
  .brand-dot { width: 58px; height: 58px; border-radius: 50%; border: 7px solid var(--white); }
  .brand-rule { width: 2px; height: 64px; background: var(--silver); opacity: .8; }
  .brand-name { font-size: 36px; font-weight: 600; letter-spacing: -.5px; }
  .hours { position: absolute; left: 40px; top: 172px; font-size: 14px; line-height: 1.45; color: var(--silver); }
  .hours h2 { color: var(--neon); font-size: 18px; font-weight: 700; margin-bottom: 2px; }
  .hours strong { font-weight: 700; color: var(--white); }
  .back-web { position: absolute; left: 40px; bottom: 26px; color: var(--neon); font-size: 14px; font-weight: 600; }
</style>
</head>
<body>
  <section class="card card-front">
    <svg class="photo-band" viewBox="0 0 540 309" preserveAspectRatio="none">
      <defs>
        <linearGradient id="shelves" x1="0" y1="0" x2="1" y2="1">
          <stop offset="0" stop-color="var(--photo-warm)"/>
          <stop offset=".45" stop-color="var(--photo-light)"/>
          <stop offset="1" stop-color="var(--photo-mid)"/>
        </linearGradient>
      </defs>
      <path role="img" aria-label="Photo of pharmacy shelves stocked with products" d="M0 0 H150 C215 70 170 200 250 309 H0 Z" fill="url(#shelves)"/>
      <path d="M150 0 C215 70 170 200 250 309 H236 C158 200 202 70 138 0 Z" fill="var(--neon)"/>
      <path d="M150 0 C215 70 170 200 250 309" fill="none" stroke="var(--white)" stroke-width="2" opacity=".6"/>
    </svg>
    <div class="contact">
      <p class="name">Vel's Apothecary</p>
      <p class="role">Owner/Pharm D.</p>
      <p class="address">7143 North Birch Lane<br>Sioux Falls, SD 57362</p>
      <p class="line"><span class="icon"><svg width="10" height="10" viewBox="0 0 10 10"><path d="M2 1h2l1 2-1 1a5 5 0 0 0 2 2l1-1 2 1v2a1 1 0 0 1-1 1A8 8 0 0 1 1 2a1 1 0 0 1 1-1z" fill="#1f1f21"/></svg></span>605-318-6027</p>
      <p class="line"><span class="icon"><svg width="10" height="10" viewBox="0 0 10 10"><rect x="2" y="1" width="6" height="3" fill="#1f1f21"/><rect x="1" y="4" width="8" height="4" fill="#1f1f21"/></svg></span>605-318-6025</p>
      <p class="line"><span class="icon"><svg width="10" height="10" viewBox="0 0 10 10"><rect x="1" y="2" width="8" height="6" fill="#1f1f21"/><path d="M1 2l4 3 4-3" stroke="#a8d32c" fill="none"/></svg></span>vel@velsapothecary.example</p>
      <p class="web">www.velsapothecary.example</p>
    </div>
  </section>

  <section class="card card-back">
    <div class="brand">
      <span class="brand-dot"></span>
      <span class="brand-rule"></span>
      <span class="brand-name">Vel's Apothecary</span>
    </div>
    <div class="hours">
      <h2>Store hours</h2>
      <p><strong>Monday-Friday</strong> 8 am- 7 pm | <strong>Saturday</strong> 8 am- 12 pm</p>
      <p><strong>Sunday</strong> Closed</p>
    </div>
    <p class="back-web">www.velsapothecary.example</p>
  </section>
</body>
</html>
```